Our brand new and excilting business, ZEPPO wares, needs a fresh, vibriant and clean website that is

We need a new website designed to sell our ZEPPO wares products to schools and fundraisers. We plan to have around 24 items with great images, add to cart and some really new and cool products. This site needs to be clean, fresh and funky, really clean lines, easy to navigate but look really fun and fresh

Target Market(s)

School fundraising. Kids

Industry/Entity Type

Business

Number of Pages Required

4 page

Colors
add136
fbee3d
fbed22
9bcb3c
f78f20

Requirements
Must have
• Fresh, fun and easy to navigate. Great shopping product page that has images of our products and add to cart
Nice to have
• Flashing image availibility
Should not have
• Must not be old and boring

```html
<!DOCTYPE html>
<html lang="en">
<head>
<meta charset="utf-8">
<title>ZEPPO wares – Glow Products for Schools &amp; Fundraisers</title>
<link rel="stylesheet" href="https://fonts.googleapis.com/css2?family=Open+Sans:wght@300;400;600;700&family=Oswald:wght@500;700&display=swap">
<style>
:root{
  --orange:#f78f20;
  --green:#9bcb3c;
  --lime:#add136;
  --yellow:#fbee3d;
  --yellow-deep:#fbed22;
  --pink:#e8308a;
  --red:#e2332f;
  --blue:#2a8fd6;
  --navy:#1b2f6b;
  --ink:#333;
  --muted:#777;
  --line:#e2e2e2;
  --panel:#f1f1f1;
  --footer:#3a3a3a;
  --footer-dark:#2b2b2b;
}
*{box-sizing:border-box;margin:0;padding:0}
html,body{width:1200px;height:3004px;overflow:hidden;background:#fff}
body{font-family:"Open Sans",Arial,sans-serif;color:var(--ink);font-size:13px}
.page{position:relative;width:1200px;height:3004px}
.wrap{width:1080px;margin:0 auto;position:relative}

/* top bar */
.topbar{height:30px;background:#fafafa;border-bottom:1px solid var(--line);font-size:11px;color:var(--muted)}
.topbar .wrap{display:flex;justify-content:space-between;align-items:center;height:30px}
.topbar strong{color:var(--red)}
.topbar .account{display:flex;gap:18px;align-items:center}
.cart-btn{background:var(--orange);color:#fff;padding:4px 14px;border-radius:3px;font-weight:600}

/* header */
.header{height:82px}
.header .wrap{display:flex;align-items:center;justify-content:space-between;height:82px}
.brand{display:flex;align-items:center;gap:10px}
.brand-dot{width:30px;height:30px;border-radius:50%;background:var(--orange)}
.brand-name{font-size:34px;font-weight:700;color:var(--orange);letter-spacing:-.5px}
.brand-tag{font-size:10px;color:var(--muted);margin-top:-4px}
.search{width:330px;height:32px;border:1px solid #ccc;border-radius:3px;display:flex;align-items:center;justify-content:space-between;padding:0 10px;color:#aaa;font-size:12px}
.service{text-align:right}
.service small{display:block;font-size:11px;color:var(--muted)}
.service b{font-size:24px;color:var(--orange);font-weight:700}

/* nav */
.nav{height:34px;background:#fff;border-bottom:4px solid var(--orange)}
.nav ul{list-style:none;display:flex;gap:4px;height:30px;align-items:flex-end}
.nav li{padding:7px 16px;color:#fff;font-size:12px;font-weight:600;border-radius:4px 4px 0 0}
.nav .t1{background:var(--orange)}.nav .t2{background:var(--blue)}.nav .t3{background:var(--green)}
.nav .t4{background:var(--yellow-deep);color:#5a4a00}.nav .t5{background:var(--pink)}.nav .t6{background:#7a47b8}.nav .t7{background:var(--red)}

/* hero */
.hero{height:362px;margin-top:4px;position:relative;background:linear-gradient(90deg,#2c2a6e 0%,#1c3f93 45%,#2369c4 100%);overflow:hidden}
.hero-photo{position:absolute;left:60px;top:0;width:520px;height:362px;background:radial-gradient(ellipse at 50% 45%,#e9b89a 0%,#b77b65 30%,#3b3b86 75%,transparent 100%)}
.hero-badge{position:absolute;left:560px;top:56px;width:92px;height:92px;border-radius:50%;background:var(--yellow);color:var(--navy);font-weight:700;font-size:15px;display:flex;align-items:center;justify-content:center;text-align:center;line-height:1.1;transform:rotate(-12deg)}
.hero-copy{position:absolute;left:648px;top:110px;color:#fff}
.hero-copy h1{font-weight:300;font-size:48px;line-height:1.1}
.btn{display:inline-block;background:var(--orange);color:#fff;font-weight:700;font-size:13px;padding:9px 22px;border-radius:3px;text-transform:uppercase}
.hero-copy .btn{margin-top:22px;background:var(--red)}

/* promises */
.promises{height:118px;border-bottom:1px solid var(--line)}
.promises .wrap{display:flex;justify-content:space-between;align-items:center;height:118px;padding:0 40px}
.promise{display:flex;align-items:center;gap:14px;font-size:13px;color:var(--muted);width:300px}
.promise b{display:block;color:var(--ink)}
.seal{width:62px;height:62px;border-radius:50%;background:var(--orange);flex:none}
.seal.gold{background:#e0a21e}

/* categories */
.categories{height:298px}
.categories .wrap{display:flex;justify-content:space-between;padding:40px 50px 0}
.cat{width:282px;height:228px;position:relative;border-radius:4px;overflow:hidden}
.cat-1{background:linear-gradient(135deg,#f7c641,#e8452e 60%,#2d63c9)}
.cat-2{background:linear-gradient(135deg,#2b2f7a,#32a7e8 50%,#9bcb3c)}
.cat-3{background:linear-gradient(135deg,#e84a8e,#f5a545 50%,#6b3aa8)}
.cat-label{position:absolute;left:50%;bottom:18px;transform:translateX(-50%);background:#fff;color:var(--navy);font-family:Oswald,sans-serif;font-size:22px;font-weight:700;padding:6px 18px;border-radius:24px;white-space:nowrap;text-transform:uppercase}
.cat-1 .cat-label{color:var(--red)}.cat-3 .cat-label{color:var(--pink)}

/* featured */
.featured{height:600px;background:var(--panel)}
.section-title{display:flex;align-items:center;justify-content:center;gap:16px;padding-top:44px}
.section-title h2{font-family:Oswald,sans-serif;font-weight:700;font-size:34px;color:#444;letter-spacing:1px}
.arrow{width:26px;height:26px;border-radius:3px;display:flex;align-items:center;justify-content:center}
.arrow.l{background:#888}.arrow.r{background:var(--orange)}
.products{display:flex;justify-content:space-between;padding:30px 54px 0}
.card{width:218px;text-align:center}
.card .shot{height:244px;border-radius:3px}
.card h3{font-size:12px;font-weight:600;margin-top:12px;color:#444}
.card .price{font-size:16px;font-weight:700;color:var(--red);margin:4px 0 10px}
.card .btn{font-size:11px;padding:7px 16px}

.s1{background:linear-gradient(160deg,#111 20%,#c23fc8 60%,#111)}
.s2{background:linear-gradient(160deg,#1a1460,#2a63e4 55%,#d23fb8)}
.s3{background:linear-gradient(160deg,#d7d7d7,#e9b38e 50%,#f2d04a)}
.s4{background:linear-gradient(160deg,#2a2a2a,#e56fa2 50%,#6fd04a)}
.s5{background:linear-gradient(160deg,#c9473b,#f4a63a 50%,#2f2f2f)}
.s6{background:linear-gradient(160deg,#101030,#e34a8c 45%,#35b2e6)}
.s7{background:linear-gradient(160deg,#e5e5e5,#f2b58a 40%,#5ba8e3)}
.s8{background:linear-gradient(160deg,#1d1d1d,#9a5be0 50%,#f4c33a)}

/* tabbed products */
.tabbed{height:542px}
.tabs{display:flex;justify-content:center;gap:10px;padding-top:40px}
.tab{border:1px solid #ccc;padding:6px 18px;font-size:11px;font-weight:700;color:#777;border-radius:3px;text-transform:uppercase}
.tab.on{background:var(--green);border-color:var(--green);color:#fff}
.tabbed .products{padding-top:30px}

/* catalogue banner */
.catalogue{height:216px;position:relative;background:linear-gradient(90deg,#4d1470,#9a1f8c 45%,#3a1160);overflow:hidden}
.catalogue-photo{position:absolute;left:150px;top:0;width:400px;height:216px;background:radial-gradient(ellipse at 50% 50%,#e2a889 0%,#9a3a8a 45%,transparent 80%)}
.catalogue-copy{position:absolute;right:150px;top:46px;text-align:right;color:#fff}
.catalogue-copy .site{font-family:Oswald,sans-serif;font-size:24px;font-weight:700;color:var(--yellow)}
.catalogue-copy .big{font-family:Oswald,sans-serif;font-size:44px;font-weight:700;line-height:1.05}
.catalogue-copy .out{font-family:Oswald,sans-serif;font-size:26px;font-weight:500;color:var(--lime)}

/* testimonials */
.testimonials{height:258px;text-align:center}
.testimonials h2{font-family:Oswald,sans-serif;font-weight:700;font-size:34px;color:#444;padding-top:38px;letter-spacing:1px}
.quote{width:820px;margin:22px auto 0;font-size:13px;color:var(--muted);line-height:1.7;position:relative}
.quote .mark{position:absolute;top:-6px;font-size:44px;color:var(--orange);font-family:Georgia,serif;line-height:1}
.quote .mark.o{left:-36px}.quote .mark.c{right:-36px}
.quote cite{display:block;margin-top:12px;font-style:normal;font-weight:700;color:var(--orange)}
.quote small{display:block;color:#999}

/* footer */
.newsletter{height:52px;background:var(--footer-dark);color:#fff}
.newsletter .wrap{display:flex;align-items:center;justify-content:space-between;height:52px;font-size:12px}
.socials{display:flex;gap:8px;align-items:center}
.socials span{width:24px;height:24px;border-radius:50%;background:#555;display:block}
.signup{display:flex;align-items:center;gap:10px}
.signup .field{width:230px;height:28px;background:#fff;border-radius:3px}
.signup .btn{padding:6px 14px;font-size:11px}
.footer{height:264px;background:var(--footer);color:#bbb}
.footer .wrap{display:flex;justify-content:space-between;padding-top:30px}
.col h4{color:#fff;font-size:12px;font-weight:700;text-transform:uppercase;margin-bottom:12px}
.col li{list-style:none;font-size:11px;line-height:2}
.bottombar{height:52px;background:#fff;border-top:1px solid var(--line);font-size:10px;color:#888}
.bottombar .wrap{display:flex;align-items:center;justify-content:space-between;height:52px}
.cards{display:flex;gap:6px}
.cards span{width:36px;height:22px;background:#ddd;border-radius:3px;display:block}
</style>
</head>
<body>
<div class="page">

<div class="topbar"><div class="wrap">
  <div><strong>3X FREE TREATS</strong> when you spend over £50 today!</div>
  <div class="account"><span>My Account</span><span>Checkout</span><span class="cart-btn">Your Basket</span></div>
</div></div>

<header class="header"><div class="wrap">
  <div>
    <div class="brand"><span class="brand-dot"></span><span class="brand-name">ZEPPO wares</span></div>
    <div class="brand-tag">The school fundraising glow specialists</div>
  </div>
  <div class="search"><span>Search for Products</span>
    <svg width="14" height="14" viewBox="0 0 14 14"><circle cx="6" cy="6" r="4.5" fill="none" stroke="#999" stroke-width="1.6"/><line x1="9.3" y1="9.3" x2="13" y2="13" stroke="#999" stroke-width="1.6"/></svg>
  </div>
  <div class="service"><small>Customer Services</small><b>0800 555 0199</b></div>
</div></header>

<nav class="nav"><div class="wrap"><ul>
  <li class="t1">Glow Articles</li><li class="t2">Light Up Novelties</li><li class="t3">Glowing Necklaces</li>
  <li class="t4">Glow Bracelets</li><li class="t5">Glow Sticks</li><li class="t6">Party Supplies</li><li class="t7">Wholesale</li>
</ul></div></nav>

<section class="hero">
  <div class="hero-photo" role="img" aria-label="Smiling girl holding a light-up star wand and glow sticks"></div>
  <div class="hero-badge">New &amp;<br>Cool</div>
  <div class="hero-copy">
    <h1>Glow Bracelets<br>Glow Necklaces<br>Glow Sticks</h1>
    <span class="btn">Shop now</span>
  </div>
</section>

<section class="promises"><div class="wrap">
  <div class="promise"><span class="seal"></span><div><b>Replace or</b>Refund Offered</div></div>
  <div class="promise"><span class="seal gold"></span><div><b>PTA and</b>Charity Discounts</div></div>
  <div class="promise">
    <svg width="62" height="44" viewBox="0 0 62 44" aria-hidden="true"><rect x="2" y="6" width="36" height="26" rx="2" fill="var(--red)"/><path d="M38 14h12l10 10v8H38z" fill="var(--red)"/><circle cx="14" cy="36" r="6" fill="#333"/><circle cx="48" cy="36" r="6" fill="#333"/></svg>
    <div><b>Next Day Special</b>Delivery Service Available...</div>
  </div>
</div></section>

<section class="categories"><div class="wrap">
  <div class="cat cat-1" role="img" aria-label="Foam flashing novelty products"><span class="cat-label">Foam Flash Novelties</span></div>
  <div class="cat cat-2" role="img" aria-label="Bundle of bright glow sticks"><span class="cat-label">Glow Sticks</span></div>
  <div class="cat cat-3" role="img" aria-label="Children enjoying a glow party"><span class="cat-label">Party Supplies</span></div>
</div></section>

<section class="featured">
  <div class="section-title">
    <span class="arrow l"><svg width="10" height="10" viewBox="0 0 10 10"><path d="M7 1L3 5l4 4" fill="none" stroke="#fff" stroke-width="2"/></svg></span>
    <h2>FEATURED PRODUCTS</h2>
    <span class="arrow r"><svg width="10" height="10" viewBox="0 0 10 10"><path d="M3 1l4 4-4 4" fill="none" stroke="#fff" stroke-width="2"/></svg></span>
  </div>
  <div class="products">
    <div class="card"><div class="shot s1" role="img" aria-label="Light up gloves glowing in the dark"></div><h3>Light Up Gloves</h3><div class="price">£4.50</div><span class="btn">Shop now</span></div>
    <div class="card"><div class="shot s2" role="img" aria-label="Neon face and body paint under UV light"></div><h3>Neon Face &amp; Body Paint</h3><div class="price">£1.99</div><span class="btn">Shop now</span></div>
    <div class="card"><div class="shot s3" role="img" aria-label="Girl holding a rainbow wand"></div><h3>Rainbow Wand</h3><div class="price">£1.47</div><span class="btn">Shop now</span></div>
    <div class="card"><div class="shot s4" role="img" aria-label="Colourful glow necklaces"></div><h3>Glow Necklaces</h3><div class="price">£0.24</div><span class="btn">Shop now</span></div>
  </div>
</section>

<section class="tabbed">
  <div class="tabs"><span class="tab on">New</span><span class="tab">Top Rated</span><span class="tab">Bestsellers</span></div>
  <div class="products">
    <div class="card"><div class="shot s5" role="img" aria-label="Crazy coloured hair spray product"></div><h3>Crazy Hair</h3><div class="price">£3.99</div><span class="btn">Shop now</span></div>
    <div class="card"><div class="shot s6" role="img" aria-label="Flashing animal soft rings"></div><h3>Flashing Animal Soft Rings</h3><div class="price">£0.98</div><span class="btn">Shop now</span></div>
    <div class="card"><div class="shot s7" role="img" aria-label="Child holding a rainbow windmill"></div><h3>Rainbow Windmill</h3><div class="price">£1.07</div><span class="btn">Shop now</span></div>
    <div class="card"><div class="shot s8" role="img" aria-label="Light up flashing hoop"></div><h3>Light Up and Flashing Hoop</h3><div class="price">£3.88</div><span class="btn">Shop now</span></div>
  </div>
</section>

<section class="catalogue">
  <div class="catalogue-photo" role="img" aria-label="Girl surrounded by glowing sticks"></div>
  <div class="catalogue-copy">
    <div class="site">zeppowares.co.uk 2015/2016</div>
    <div class="big">New Catalogue</div>
    <div class="out">Out Now!</div>
  </div>
</section>

<section class="testimonials">
  <h2>WHAT THEY SAY</h2>
  <div class="quote">
    <span class="mark o">“</span><span class="mark c">”</span>
    Your new website is so easy to navigate and the ordering process is quick and simple. The glow products arrived the very next day and were a huge hit at our school disco. Thank you for the fantastic service, we will certainly be ordering again.
    <cite>Mary T</cite><small>12th October 2015</small>
  </div>
</section>

<div class="newsletter"><div class="wrap">
  <div class="socials"><span style="margin-right:6px;width:auto;height:auto;background:none">Go to the shop</span><span></span><span></span><span></span><span></span></div>
  <div class="signup"><span>Sign up to our newsletter</span><span class="field"></span><span class="btn">Subscribe</span></div>
</div></div>

<footer class="footer"><div class="wrap">
  <div class="col"><h4>Customer Service</h4><ul><li>Contact Us</li><li>Delivery Information</li><li>Returns</li><li>Order Tracking</li><li>Site Map</li><li>FAQs</li></ul></div>
  <div class="col"><h4>Wholesale Products</h4><ul><li>Wholesale Glow Sticks</li><li>Wholesale Bracelets</li><li>Wholesale Necklaces</li><li>Party Packs</li><li>Bulk Orders</li></ul></div>
  <div class="col"><h4>Help and Information</h4><ul><li>School Fundraising Ideas</li><li>Glow Stick Safety</li><li>PTA Discounts</li><li>Charity Support</li><li>Product Guides</li></ul></div>
  <div class="col"><h4>Our Services</h4><ul><li>Next Day Delivery</li><li>Trade Accounts</li><li>Gift Vouchers</li><li>Catalogue Request</li></ul></div>
  <div class="col"><h4>Policies</h4><ul><li>Privacy Policy</li><li>Terms of Use</li><li>Cookie Policy</li><li>Returns Policy</li></ul></div>
</div></footer>

<div class="bottombar"><div class="wrap">
  <div class="cards"><span></span><span></span><span></span><span></span></div>
  <div>© 2015 ZEPPO wares. All rights reserved. Registered in England.</div>
</div></div>

</div>
</body>
</html>
```